Industrial / automotive service company
Renewing and reconditioning solutions
Simple
Ted Pelkin
VP - Industrial Division
217 Marston Crescent NW
Calgary, Alberta
T2P 4G6
t-pelkin@zorvamail.com

```html
<!DOCTYPE html>
<html lang="en">
<head>
<meta charset="utf-8">
<title>Tovalmex Services Inc. – Business Card</title>
<link rel="stylesheet" href="https://fonts.googleapis.com/css2?family=Michroma&display=swap">
<style>
  :root {
    --page-bg: #e6e7e4;
    --card-bg: #f3f4f1;
    --brand-green: #8cc63f;
    --brand-green-dark: #76ad2f;
    --silver-light: #f2f3f3;
    --silver-mid: #c9cccd;
    --silver-dark: #9ea3a5;
    --ink-grey: #8a8f91;
    --white: #ffffff;
  }
  * { margin: 0; padding: 0; box-sizing: border-box; }
  html, body {
    width: 1200px; height: 768px; overflow: hidden;
    background: var(--page-bg);
    font-family: "Michroma", "Arial", sans-serif;
  }
  .card {
    position: absolute; left: 75px; top: 84px;
    width: 1050px; height: 600px;
    background: var(--card-bg);
    border-radius: 6px;
    overflow: hidden;
    box-shadow: 0 8px 30px rgba(0,0,0,0.12);
  }
  .brand {
    position: absolute; left: 150px; top: 120px;
    display: flex; align-items: center; gap: 22px;
  }
  .brand-dot {
    width: 46px; height: 46px; border-radius: 50%;
    background: var(--brand-green);
  }
  .brand-name {
    color: var(--brand-green-dark);
    font-size: 46px; letter-spacing: 2px; line-height: 1;
  }
  .silver-bar {
    position: absolute; left: 0; width: 100%;
    background: linear-gradient(to bottom, var(--silver-light), var(--silver-mid) 55%, var(--silver-dark));
  }
  .silver-bar.top { top: 318px; height: 16px; }
  .silver-bar.bottom { top: 528px; height: 22px; }
  .green-band {
    position: absolute; left: 0; top: 334px; width: 100%; height: 194px;
    background: var(--brand-green);
  }
  .notch {
    position: absolute; left: 156px; top: 0;
    width: 0; height: 0;
    border-left: 16px solid transparent; border-right: 16px solid transparent;
    border-top: 18px solid var(--silver-mid);
  }
  .person {
    position: absolute; left: 70px; top: 64px;
    color: var(--white); text-align: center; width: 340px;
  }
  .person-name { font-size: 17px; letter-spacing: 2px; }
  .person-title { font-size: 14px; letter-spacing: 1.5px; margin-top: 14px; }
  .divider {
    position: absolute; left: 530px; top: 22px; width: 2px; height: 150px;
    background: rgba(255,255,255,0.75);
  }
  .contact {
    position: absolute; left: 560px; top: 24px;
    list-style: none; color: var(--white);
    font-size: 11px; letter-spacing: 1.5px; line-height: 19px;
  }
  .contact li { display: flex; align-items: flex-start; gap: 10px; margin-bottom: 4px; }
  .contact svg { flex: none; margin-top: 2px; }
  .card-foot {
    position: absolute; left: 0; top: 550px; width: 100%; height: 50px;
    background: var(--card-bg);
  }
</style>
</head>
<body>
  <div class="card">
    <div class="brand">
      <span class="brand-dot"></span>
      <span class="brand-name">TOVALMEX SERVICES INC.</span>
    </div>

    <div class="silver-bar top"></div>

    <section class="green-band">
      <span class="notch"></span>
      <div class="person">
        <p class="person-name">Ted Pelkin</p>
        <p class="person-title">VP - Industrial Division</p>
      </div>
      <span class="divider"></span>
      <ul class="contact">
        <li>
          <svg width="15" height="15" viewBox="0 0 16 16"><circle cx="8" cy="8" r="8" fill="#fff"/><path d="M8 3.5a3 3 0 0 0-3 3c0 2.2 3 5.8 3 5.8s3-3.6 3-5.8a3 3 0 0 0-3-3z" fill="#8cc63f"/><circle cx="8" cy="6.5" r="1.1" fill="#fff"/></svg>
          <span>217 Marston Crescent NW<br>Calgary, Alberta<br>T2P 4G6</span>
        </li>
        <li>
          <svg width="15" height="15" viewBox="0 0 16 16"><circle cx="8" cy="8" r="8" fill="#fff"/><path d="M5.2 4h1.6l.8 2-1 .8a5 5 0 0 0 2.6 2.6l.8-1 2 .8v1.6c0 .5-.4.8-.9.8A7.1 7.1 0 0 1 4.4 4.9c0-.5.3-.9.8-.9z" fill="#8cc63f"/></svg>
          <span>(403) 555-0147</span>
        </li>
        <li>
          <svg width="15" height="15" viewBox="0 0 16 16"><circle cx="8" cy="8" r="8" fill="#fff"/><rect x="4" y="5" width="8" height="6" fill="#8cc63f"/><path d="M4 5l4 3.2L12 5" stroke="#fff" stroke-width="0.9" fill="none"/></svg>
          <span>t-pelkin@zorvamail.com</span>
        </li>
        <li>
          <svg width="15" height="15" viewBox="0 0 16 16"><circle cx="8" cy="8" r="8" fill="#fff"/><circle cx="8" cy="8" r="4" fill="none" stroke="#8cc63f" stroke-width="1.1"/><path d="M4 8h8M8 4c-1.6 2.4-1.6 5.6 0 8M8 4c1.6 2.4 1.6 5.6 0 8" stroke="#8cc63f" stroke-width="0.9" fill="none"/></svg>
          <span>www.tovalmexsvc.com</span>
        </li>
      </ul>
    </section>

    <div class="silver-bar bottom"></div>
    <div class="card-foot"></div>
  </div>
</body>
</html>
```